Construction company that specializes in roofing and siding

https://havenridgeroofs.example/featured-projects/

https://www.pinecrestrenovationllc.example/#

https://www.ironmeadowhomes.example/residential-siding-services/

Please model a website after these examples
I posted a doc that has some content to get you started. I will upload more content and photos as the site progresses.

Coded - Design and coding required

5+ page

```html
<!DOCTYPE html>
<html lang="en">
<head>
<meta charset="utf-8">
<title>Stonefield Construction — Roofing &amp; Siding in Minnesota</title>
<link rel="stylesheet" href="https://fonts.googleapis.com/css2?family=Krona+One&family=Inter:wght@400;500;600;700&display=swap">
<style>
:root{
  --ink:#111111;
  --text:#2b2b2b;
  --muted:#777777;
  --white:#ffffff;
  --dark:#555555;
  --bar:#4a4a4a;
  --line:#8a8a8a;
  --soft:#f5f5f5;
  --star:#f4a623;
}
*{box-sizing:border-box;margin:0;padding:0}
html,body{width:1200px;height:5226px;overflow:hidden}
body{font-family:"Inter",sans-serif;color:var(--text);background:var(--white);position:relative}
.abs{position:absolute}
.display{font-family:"Krona One",sans-serif;text-transform:uppercase;letter-spacing:.02em;font-weight:400}
.eyebrow{font-family:"Krona One",sans-serif;text-transform:uppercase;font-size:11px;letter-spacing:.12em}
.btn{display:inline-flex;align-items:center;justify-content:center;gap:8px;font-size:12px;font-weight:600;text-transform:uppercase;letter-spacing:.02em;text-decoration:none;border-radius:3px}
.btn-dark{background:var(--ink);color:var(--white)}
.btn-outline{border:1.5px solid currentColor;background:transparent}
.btn svg{width:12px;height:10px}
.ph{display:block}
section,header.header,footer.footer{position:absolute;left:0;width:1200px}

/* top bar */
.topbar{top:0;height:46px;background:var(--bar);color:var(--white);font-size:13px}
.topbar .contact{left:84px;top:14px;display:flex;gap:22px}
.topbar .social{right:120px;top:14px;display:flex;gap:12px}
.dot{width:14px;height:14px;border:1.5px solid var(--white);border-radius:50%}

/* header */
.header{top:46px;height:106px;background:var(--white)}
.brand{display:flex;align-items:center;gap:12px}
.brand .mark{width:56px;height:56px;background:#5a5a5a;border-radius:4px}
.brand .name{font-family:"Krona One",sans-serif;font-size:19px;line-height:1.05;color:#4a4a4a;text-transform:uppercase}
.brand .name small{display:block;font-size:11px;letter-spacing:.1em}
.header .brand{left:84px;top:24px}
.nav{right:86px;top:26px;display:flex;align-items:center;gap:28px;font-size:14px;color:var(--ink)}
.nav .btn{height:48px;padding:0 22px;font-size:11px}

/* hero */
.hero{top:152px;height:660px}
.hero .photo{position:absolute;inset:0;background:linear-gradient(180deg,#5b6470 0%,#8a8d8f 45%,#b7a98f 75%,#7d8a5e 100%)}
.hero .cut{position:absolute;left:0;bottom:0;width:1200px;height:160px}
.hero .eyebrow{left:84px;top:118px;color:var(--white);font-size:15px;letter-spacing:.06em}
.hero h1{left:84px;top:146px;color:var(--white);font-size:33px;line-height:47px;width:640px}
.hero .btn{left:84px;top:312px;height:48px;width:168px;color:var(--white)}

/* about */
.about{top:812px;height:654px}
.about .emblem{left:84px;top:92px;width:428px;height:450px;border-radius:40px;background:radial-gradient(circle at 50% 50%,#6f7a86 0%,#4d5560 40%,#8a8a8a 75%,#5e5e5e 100%)}
.about .eyebrow{left:554px;top:154px;color:var(--ink)}
.about h2{left:554px;top:180px;font-size:28px;color:var(--ink)}
.about .lead{left:554px;top:222px;font-size:15px;font-weight:500;color:var(--ink)}
.about p.body{left:554px;top:258px;width:560px;font-size:14px;line-height:24px}
.about .btn{left:554px;top:412px;width:216px;height:46px}

/* services */
.services{top:1466px;height:660px;background:var(--dark);color:var(--white)}
.center{left:0;width:1200px;text-align:center}
.services .eyebrow{top:74px}
.services h2{top:92px;font-size:28px}
.svc{top:151px;width:320px;height:443px;border:1px solid #6e6e6e}
.svc .ph{height:201px;background:linear-gradient(160deg,#9db3c8,#5c6570)}
.svc h3{margin:24px 0 0 24px;font-size:18px;font-weight:600}
.svc ul{list-style:none;margin:14px 0 0 24px;font-size:14px}
.svc li{height:30px;display:flex;align-items:center;gap:10px}
.svc li svg{width:6px;height:10px}
.svc .btn{position:absolute;left:22px;top:376px;width:156px;height:46px;color:var(--white)}

/* works */
.works{top:2126px;height:700px}
.works .eyebrow{top:38px;color:var(--ink)}
.works h2{top:58px;font-size:28px;color:var(--ink)}
.work{border-radius:14px}
.works .btn{left:522px;top:609px;width:155px;height:45px}

/* testimonials */
.reviews{top:2826px;height:610px;background:var(--dark);color:var(--white)}
.reviews .eyebrow{top:88px}
.reviews h2{top:114px;font-size:28px;line-height:36px}
.card{top:227px;width:326px;height:232px;background:var(--white);color:var(--text);padding:20px}
.card .who{display:flex;align-items:center;gap:12px;font-size:14px;font-weight:600;color:var(--ink)}
.card .avatar{width:46px;height:46px;border-radius:50%;background:#c9c9c9}
.card p{margin-top:14px;font-size:14px;line-height:24px}
.card .meta{position:absolute;left:24px;right:22px;bottom:22px;display:flex;justify-content:space-between;font-size:12px;font-weight:600}
.stars{color:var(--star);letter-spacing:2px}
.arrows{left:550px;top:490px;display:flex;gap:14px}

/* team */
.team{top:3436px;height:666px;background:var(--soft)}
.team h2{top:78px;font-size:30px;line-height:36px;color:var(--ink)}
.team .intro{top:154px;font-size:14px;line-height:22px;color:#555}
.member{top:252px;width:208px;text-align:center}
.member .ph{height:240px;background:linear-gradient(180deg,#c9cbc7,#7d8a9c)}
.member h3{margin-top:20px;font-size:18px;font-weight:600;color:var(--ink)}
.member span{font-size:13px;font-style:italic;color:var(--muted)}

/* blog */
.blog{top:4102px;height:660px;background:var(--dark);color:var(--white)}
.blog .eyebrow{left:84px;top:104px}
.blog h2{left:84px;top:126px;font-size:28px}
.blog .btn{left:958px;top:120px;width:156px;height:46px;color:var(--white)}
.post{top:196px;width:330px}
.post .ph{height:258px;border:1px solid #7d7d7d;background:linear-gradient(160deg,#a9b8c6,#4d5864)}
.post .date{margin-top:18px;font-size:11px;font-weight:600}
.post h3{margin-top:8px;font-size:18px;line-height:27px;font-weight:600}

/* footer */
.footer{top:4762px;height:464px}
.footer .brand{left:84px;top:66px}
.footer .about-text{left:84px;top:138px;width:300px;font-size:14px;line-height:24px}
.footer .social{left:144px;top:262px;display:flex;gap:14px}
.footer .social span{width:36px;height:36px;border:1.5px solid var(--ink);border-radius:50%}
.fcol{top:78px}
.fcol h4{font-family:"Krona One",sans-serif;font-size:12px;text-transform:uppercase;color:var(--ink);letter-spacing:.05em}
.fcol ul{list-style:none;margin-top:28px;font-size:14px;line-height:31px}
.fnav{left:0;top:336px;width:1200px;height:58px;border-top:1px solid #bbb;border-bottom:1px solid #bbb;display:flex;justify-content:center}
.fnav a{display:flex;align-items:center;padding:0 28px;font-size:13px;letter-spacing:.12em;text-transform:uppercase;color:var(--ink);text-decoration:none;border-left:1px solid #bbb}
.fnav a:first-child{border-left:0}
.copy{left:84px;top:425px;font-size:12px}
</style>
</head>
<body>

<section class="topbar">
  <div class="abs contact">
    <span>&#9990; 1800-555-017</span>
    <span>&#9993; info@stonefieldbuild.example</span>
  </div>
  <div class="abs social" aria-label="Social links">
    <span class="dot"></span><span class="dot"></span><span class="dot"></span>
  </div>
</section>

<header class="header">
  <div class="abs brand">
    <span class="mark"></span>
    <span class="name">Stonefield<small>Construction</small></span>
  </div>
  <nav class="abs nav">
    <span>Home</span><span>About</span><span>What we do</span><span>Blog</span><span>Contact</span>
    <a class="btn btn-dark" href="#">Get free inspection
      <svg viewBox="0 0 12 10"><path d="M0 5h10M6 1l4 4-4 4" stroke="currentColor" stroke-width="1.6" fill="none"/></svg></a>
  </nav>
</header>

<section class="hero">
  <div class="photo" role="img" aria-label="Two-storey stone house with a dark shingle roof under a dramatic sky"></div>
  <svg class="cut" viewBox="0 0 1200 160" preserveAspectRatio="none"><polygon points="0,0 600,130 1200,0 1200,160 0,160" fill="#fff"/></svg>
  <div class="abs eyebrow">Stonefield Construction</div>
  <h1 class="abs display">Is your source for roofing and siding in Minnesota</h1>
  <a class="abs btn btn-outline" href="#">Contact us
    <svg viewBox="0 0 12 10"><path d="M0 5h10M6 1l4 4-4 4" stroke="currentColor" stroke-width="1.6" fill="none"/></svg></a>
</section>

<section class="about">
  <div class="abs emblem" role="img" aria-label="Shield-shaped frame showing roofers installing standing seam metal roofing"></div>
  <div class="abs eyebrow">About</div>
  <h2 class="abs display">Stonefield Construction</h2>
  <div class="abs lead">From humble beginnings</div>
  <p class="abs body">In 2016 Carl Brenner started helping people with their home improvement projects. His very first job was installing window trim for a wonderful homeowner in Forest lake MN. He did his best work and made sure he treated his first customer like family. Afterall, his first customer was Ruth Brenner, his Mom.</p>
  <a class="abs btn btn-dark" href="#">Get free inspection
    <svg viewBox="0 0 12 10"><path d="M0 5h10M6 1l4 4-4 4" stroke="currentColor" stroke-width="1.6" fill="none"/></svg></a>
</section>

<section class="services">
  <div class="abs center eyebrow">Services</div>
  <h2 class="abs center display">What we do</h2>

  <article class="abs svc" style="left:84px">
    <div class="ph" role="img" aria-label="Roofer working on a pitched shingle roof"></div>
    <h3>Roofing</h3>
    <ul>
      <li><svg viewBox="0 0 6 10"><path d="M1 1l4 4-4 4" stroke="#fff" fill="none" stroke-width="1.3"/></svg>Architectural shingles</li>
      <li><svg viewBox="0 0 6 10"><path d="M1 1l4 4-4 4" stroke="#fff" fill="none" stroke-width="1.3"/></svg>Standing seam steel roofing</li>
      <li><svg viewBox="0 0 6 10"><path d="M1 1l4 4-4 4" stroke="#fff" fill="none" stroke-width="1.3"/></svg>Agricultural steel roofing</li>
    </ul>
    <a class="btn btn-outline" href="#">Learn more <svg viewBox="0 0 12 10"><path d="M0 5h10M6 1l4 4-4 4" stroke="currentColor" stroke-width="1.6" fill="none"/></svg></a>
  </article>

  <article class="abs svc" style="left:440px">
    <div class="ph" role="img" aria-label="Worker in a hard hat fitting a gutter under the eaves"></div>
    <h3>Siding</h3>
    <ul>
      <li><svg viewBox="0 0 6 10"><path d="M1 1l4 4-4 4" stroke="#fff" fill="none" stroke-width="1.3"/></svg>Vinyl siding</li>
      <li><svg viewBox="0 0 6 10"><path d="M1 1l4 4-4 4" stroke="#fff" fill="none" stroke-width="1.3"/></svg>Ribbed steel siding</li>
      <li><svg viewBox="0 0 6 10"><path d="M1 1l4 4-4 4" stroke="#fff" fill="none" stroke-width="1.3"/></svg>Engineered wood siding</li>
    </ul>
    <a class="btn btn-outline" href="#">Learn more <svg viewBox="0 0 12 10"><path d="M0 5h10M6 1l4 4-4 4" stroke="currentColor" stroke-width="1.6" fill="none"/></svg></a>
  </article>

  <article class="abs svc" style="left:794px">
    <div class="ph" role="img" aria-label="Repair technician holding a cordless drill"></div>
    <h3>Repair</h3>
    <ul>
      <li><svg viewBox="0 0 6 10"><path d="M1 1l4 4-4 4" stroke="#fff" fill="none" stroke-width="1.3"/></svg>Missing shingles</li>
      <li><svg viewBox="0 0 6 10"><path d="M1 1l4 4-4 4" stroke="#fff" fill="none" stroke-width="1.3"/></svg>Leaking roof</li>
      <li><svg viewBox="0 0 6 10"><path d="M1 1l4 4-4 4" stroke="#fff" fill="none" stroke-width="1.3"/></svg>Add vents</li>
    </ul>
    <a class="btn btn-outline" href="#">Learn more <svg viewBox="0 0 12 10"><path d="M0 5h10M6 1l4 4-4 4" stroke="currentColor" stroke-width="1.6" fill="none"/></svg></a>
  </article>
</section>

<section class="works">
  <div class="abs center eyebrow">Featured work</div>
  <h2 class="abs center display">Best works all time</h2>
  <div class="abs work ph" style="left:84px;top:107px;width:551px;height:484px;background:linear-gradient(180deg,#6f9fd0 0%,#4a4f55 45%,#2c2f33 100%)" role="img" aria-label="Dark tile roof with a skylight against blue sky"></div>
  <div class="abs work ph" style="left:657px;top:107px;width:457px;height:232px;background:linear-gradient(160deg,#cfdbe8,#7e95b0 60%,#3b4048)" role="img" aria-label="Roof eave with soffit and gutter seen from below"></div>
  <div class="abs work ph" style="left:657px;top:357px;width:457px;height:234px;background:linear-gradient(120deg,#e7e7e7,#f6f6f6 60%,#9fae86)" role="img" aria-label="Bright white room with a desk and tall windows"></div>
  <a class="abs btn btn-dark" href="#">View all <svg viewBox="0 0 12 10"><path d="M0 5h10M6 1l4 4-4 4" stroke="currentColor" stroke-width="1.6" fill="none"/></svg></a>
</section>

<section class="reviews">
  <div class="abs center eyebrow">Featured work</div>
  <h2 class="abs center display">We’re trusted by<br>our clients</h2>

  <article class="abs card" style="left:84px">
    <div class="who"><span class="avatar" role="img" aria-label="Client portrait"></span>Marcus Hale</div>
    <p>Lorem ipsum dolor sit amet, consectetur adipiscing elit. Nulla odio massa, dapibus in congue ac, conditum eget ex. Integer tincidunt tortor eu libero pulvinar</p>
    <div class="meta"><span>2 days ago</span><span class="stars">★★★★★</span></div>
  </article>
  <article class="abs card" style="left:438px">
    <div class="who"><span class="avatar" role="img" aria-label="Client portrait"></span>Elena Ford</div>
    <p>Lorem ipsum dolor sit amet, consectetur adipiscing elit. Nulla odio massa, dapibus in congue ac, conditum eget ex. Integer tincidunt tortor eu libero pulvinar</p>
    <div class="meta"><span>1 days ago</span><span class="stars">★★★★★</span></div>
  </article>
  <article class="abs card" style="left:788px">
    <div class="who"><span class="avatar" role="img" aria-label="Client portrait"></span>Marcus Hale</div>
    <p>Lorem ipsum dolor sit amet, consectetur adipiscing elit. Nulla odio massa, dapibus in congue ac, conditum eget ex. Integer tincidunt tortor eu libero pulvinar</p>
    <div class="meta"><span>2 days ago</span><span class="stars">★★★★★</span></div>
  </article>

  <div class="abs arrows">
    <svg width="44" height="14" viewBox="0 0 44 14"><path d="M43 7H2M8 1L2 7l6 6" stroke="#ddd" stroke-width="1.6" fill="none"/></svg>
    <svg width="44" height="14" viewBox="0 0 44 14"><path d="M1 7h41M36 1l6 6-6 6" stroke="#fff" stroke-width="1.6" fill="none"/></svg>
  </div>
</section>

<section class="team">
  <h2 class="abs center display">Our experts<br>team members</h2>
  <p class="abs center intro">Phasellus molestie aliquet libero, nec vestibulum lacus fermentum euismod. Nulla<br>ut lorem arcu. Aliquam ullamcorper auctor lobortis.</p>

  <div class="abs member" style="left:84px"><div class="ph" role="img" aria-label="Team member in a yellow hard hat with arms crossed"></div><h3>Owen Price</h3><span>Seniour Member</span></div>
  <div class="abs member" style="left:358px"><div class="ph" role="img" aria-label="Team member in a hard hat and safety vest"></div><h3>Nora Price</h3><span>Seniour Member</span></div>
  <div class="abs member" style="left:634px"><div class="ph" role="img" aria-label="Team member in a hard hat and blue shirt with vest"></div><h3>Owen Price</h3><span>Seniour Member</span></div>
  <div class="abs member" style="left:908px"><div class="ph" role="img" aria-label="Team member in a yellow hard hat and safety vest"></div><h3>Owen Price</h3><span>Seniour Member</span></div>
</section>

<section class="blog">
  <div class="abs eyebrow">Blog &amp; articles</div>
  <h2 class="abs display">Our latest blog</h2>
  <a class="abs btn btn-outline" href="#">View all <svg viewBox="0 0 12 10"><path d="M0 5h10M6 1l4 4-4 4" stroke="currentColor" stroke-width="1.6" fill="none"/></svg></a>

  <article class="abs post" style="left:84px"><div class="ph" role="img" aria-label="Roofer fastening metal roof panels"></div><div class="date">2 JUNE 2024</div><h3>Suspendisse commodo sollicitudin volutpat dictum</h3></article>
  <article class="abs post" style="left:434px"><div class="ph" role="img" aria-label="Worker kneeling on a standing seam roof"></div><div class="date">2 JUNE 2024</div><h3>Suspendisse commodo sollicitudin volutpat dictum</h3></article>
  <article class="abs post" style="left:784px"><div class="ph" role="img" aria-label="Pressure washer cleaning a roof gutter"></div><div class="date">2 JUNE 2024</div><h3>Suspendisse commodo sollicitudin volutpat dictum</h3></article>
</section>

<footer class="footer">
  <div class="abs brand">
    <span class="mark"></span>
    <span class="name">Stonefield<small>Construction</small></span>
  </div>
  <p class="abs about-text">In 2016 Carl Brenner started helping people with their home improvement projects. His very first job was installing window trim for a wonderful</p>
  <div class="abs social" aria-label="Social links"><span></span><span></span><span></span></div>

  <div class="abs fcol" style="left:457px"><h4>Services</h4><ul><li>Roofing</li><li>Siding</li><li>Gutters</li><li>Windows</li><li>Repair</li></ul></div>
  <div class="abs fcol" style="left:644px"><h4>Useful links</h4><ul><li>Privacy Policy</li><li>Terms &amp; Condition</li><li>Sitemap</li><li>Other</li></ul></div>
  <div class="abs fcol" style="left:876px"><h4>Contact us</h4><ul><li>hello@stonefieldbuild.example</li><li>1800 555 017</li></ul></div>

  <nav class="abs fnav"><a href="#">Home</a><a href="#">About</a><a href="#">What we do</a><a href="#">Blog</a><a href="#">Contact</a></nav>
  <div class="abs copy">© 2024 <strong>Stonefield Construction.</strong> All right reserved</div>
</footer>

</body>
</html>
```